Consulting company with focus on aviation needs

We need a new business card design for our company. The company consults with multiple players in the industry like manufacturers and airlines. It is also a supplier and an inter-company level. Given the targeted industry (aviation) it should be both kind of serious, sound, secure, classy, ​​but also a bit technical, innovative. Should not be too playful, however, "fresh", "airy", "ligth" and "suprising" are suitabe attributes. The existing logo shall be used.

Airlines

```html
<!DOCTYPE html>
<html lang="en">
<head>
<meta charset="utf-8">
<title>Norvela – Business Card</title>
<link href="https://fonts.googleapis.com/css2?family=Exo+2:wght@400;500&display=swap" rel="stylesheet">
<style>
  :root {
    --stage: #707070;
    --paper: #ffffff;
    --orange: #f09c10;
    --teal: #239c80;
    --green: #a6ba50;
    --ink: #6e6e6e;
    --ink-strong: #737373;
  }
  * { margin: 0; padding: 0; box-sizing: border-box; }
  html, body { width: 1016px; height: 1200px; overflow: hidden; }
  body {
    background: var(--stage);
    font-family: "Exo 2", sans-serif;
    color: var(--ink);
    position: relative;
  }
  .card {
    position: absolute;
    left: 69px;
    width: 888px;
    height: 511px;
    background: var(--paper);
    overflow: hidden;
  }
  .card--front { top: 50px; }
  .card--back { top: 618px; }
  .card__shapes { position: absolute; inset: 0; width: 888px; height: 511px; }

  .brand {
    position: absolute;
    left: 0; right: 0;
    text-align: center;
  }
  .brand__dot {
    display: block;
    margin: 0 auto;
    border-radius: 50%;
    background: var(--teal);
  }
  .brand__name {
    display: block;
    color: var(--ink-strong);
    font-weight: 500;
    line-height: 1;
  }
  .brand__tagline {
    display: block;
    color: var(--orange);
    font-weight: 500;
    line-height: 1;
  }

  .card--front .brand { top: 109px; }
  .card--front .brand__dot { width: 100px; height: 100px; margin-bottom: 23px; }
  .card--front .brand__name { font-size: 48px; letter-spacing: 9px; padding-left: 9px; }
  .card--front .brand__tagline { font-size: 17px; margin-top: 4px; }

  .about {
    position: absolute;
    top: 369px; left: 0; right: 0;
    text-align: center;
    font-size: 18px;
    line-height: 27px;
  }

  .card--back .brand { top: 72px; }
  .card--back .brand__dot { width: 70px; height: 70px; margin-bottom: 10px; }
  .card--back .brand__name { font-size: 31px; letter-spacing: 6px; padding-left: 6px; }
  .card--back .brand__tagline { font-size: 12px; margin-top: 4px; }

  .person {
    position: absolute;
    top: 250px; left: 0; right: 0;
    text-align: center;
  }
  .person__name { font-size: 38px; line-height: 44px; font-weight: 400; color: var(--ink-strong); }
  .person__role { font-size: 24px; line-height: 34px; margin-top: 2px; }

  .contact {
    position: absolute;
    display: flex;
    align-items: center;
    font-size: 19px;
    line-height: 27px;
  }
  .contact svg { flex: none; }
  .contact--address { left: 74px; top: 390px; }
  .contact--address svg { margin-right: 20px; }
  .contact--phone { left: 350px; top: 404px; }
  .contact--phone svg { margin-right: 16px; }
  .contact--email { left: 562px; top: 408px; }
  .contact--email svg { margin-right: 16px; }
</style>
</head>
<body>

<section class="card card--front">
  <svg class="card__shapes" viewBox="0 0 888 511" aria-hidden="true">
    <path fill="var(--orange)"
      d="M0,0 L55,0 A430,430 0 0 1 100,511 L48,511 A380,380 0 0 0 0,198 Z"/>
    <path fill="var(--teal)"
      d="M535,0 L602,0 A430,330 0 0 0 888,86 L888,246 A395,395 0 0 1 535,0 Z"/>
  </svg>
  <div class="brand">
    <span class="brand__dot"></span>
    <span class="brand__name">NORVELA</span>
    <span class="brand__tagline">Bridging Teams - Building Strategies</span>
  </div>
  <p class="about">
    Independent advisory studio<br>
    specialising in Strategy and (Digital) Transformation<br>
    for the Aviation Industry and more.
  </p>
</section>

<section class="card card--back">
  <svg class="card__shapes" viewBox="0 0 888 511" aria-hidden="true">
    <path fill="var(--green)"
      d="M171,0 L263,0 A270,270 0 0 1 0,206 L0,168 A240,240 0 0 0 171,0 Z"/>
    <path fill="var(--orange)"
      d="M783,0 L799,0 A230,230 0 0 0 888,208 L888,326 A250,250 0 0 1 783,0 Z"/>
  </svg>
  <div class="brand">
    <span class="brand__dot"></span>
    <span class="brand__name">NORVELA</span>
    <span class="brand__tagline">Bridging Teams - Building Strategies</span>
  </div>
  <div class="person">
    <h1 class="person__name">Daniel Hartmann</h1>
    <p class="person__role">executive manager</p>
  </div>

  <div class="contact contact--address">
    <svg width="38" height="40" viewBox="0 0 38 40" aria-hidden="true">
      <path fill="var(--teal)" d="M0,14 A8,8 0 0 1 16,14 V32 H0 Z"/>
      <path fill="var(--teal)" d="M12,6 H30 A8,8 0 0 1 38,14 V32 H22 V40 H16 V14 A8,8 0 0 0 12,6 Z"/>
      <rect x="20" y="0" width="3" height="14" fill="var(--teal)"/>
      <rect x="20" y="0" width="9" height="5" fill="var(--teal)"/>
    </svg>
    <span>Street adress<br>Hamburg</span>
  </div>

  <div class="contact contact--phone">
    <svg width="38" height="38" viewBox="0 0 38 38" aria-hidden="true">
      <circle cx="19" cy="19" r="19" fill="var(--teal)"/>
      <path fill="#fff" d="M12.5,10 L16,9.5 L18,14.5 L15.8,16.2 C16.8,18.8 19,21 21.6,22 L23.4,19.8 L28.3,21.8 L27.8,25.4 C27.5,27 26,27.8 24.4,27.5 C17.5,26 11.8,20.3 10.4,13.4 C10.1,11.8 11,10.3 12.5,10 Z"/>
    </svg>
    <span>888 88 88</span>
  </div>

  <div class="contact contact--email">
    <svg width="38" height="28" viewBox="0 0 38 28" aria-hidden="true">
      <rect width="38" height="28" fill="var(--teal)"/>
      <path d="M1.5,1.5 L19,16 L36.5,1.5 M1.5,26.5 L14,12 M36.5,26.5 L24,12" fill="none" stroke="#fff" stroke-width="2"/>
    </svg>
    <span>contact@example.com</span>
  </div>
</section>

</body>
</html>
```